Brackenford Guard Service Business Card Design

Hi All

We have decided to update this project from the Meridale Protection and Patrol Outfitters to the one mentioned above.

We are a company that supplies guard services .
Updates

Project Deadline Extended
Reason: Since we have changed the projet to a new design and idea this gives veryone more time. we are all busy regards colin

please include the following details on the card

 Master License 536918407 or M/L 536918407

phone 02 7163 2987

the logo can be removed from the shield , ie scales and eagle with the writing    etc

thank you                       

Hi All

There are great design that have come in so far and thank you for your time and design.

Please adjust the design to include

Company Name

Name  - Colin Parsnow

Address - PO Box 358 Elmcrest 2061

Master License Number - 536 918 407

ABN - 62417 390518 

Web address  www.brackenfordguardservice.com.au

email -  security@brackenfordguardservice.com.au

Thank you

Colin

                                   

Target Market(s)

Commercial, Residential, Business, Government, Corporate

Industry/Entity Type

Business

Contact Information for Business Card

Colin Parsnow
General Manager 0438 725 914
ABN 62 417 390 518 0271632987
PO Box 358
Elmcrest 2061

www.brackenfordguardservice.com.au

Requirements
Must have
• the company logo as per attachment below

```html
<!DOCTYPE html>
<html lang="en">
<head>
<meta charset="utf-8">
<title>Brackenford Guard Service – Business Card</title>
<link href="https://fonts.googleapis.com/css2?family=Lato:wght@400;700;900&display=swap" rel="stylesheet">
<style>
  :root {
    --navy: #16244a;
    --gold: #f6c416;
    --white: #ffffff;
    --paper: #fbfbfa;
    --backdrop: #e4e4e2;
    --shadow: rgba(0, 0, 0, 0.18);
  }
  * { box-sizing: border-box; margin: 0; padding: 0; }
  html, body {
    width: 1200px;
    height: 900px;
    overflow: hidden;
    background: var(--backdrop);
    font-family: "Lato", Arial, sans-serif;
  }
  .stage {
    position: relative;
    width: 1200px;
    height: 900px;
  }
  .card {
    position: absolute;
    left: 300px;
    width: 600px;
    height: 367px;
    background: var(--paper);
    box-shadow: 0 10px 30px var(--shadow);
    overflow: hidden;
  }
  .card--front { top: 58px; }
  .card--back { top: 475px; display: flex; }

  /* Brand name set in place of the mark */
  .brand {
    display: flex;
    flex-direction: column;
    align-items: center;
    gap: 14px;
    text-align: center;
    color: var(--navy);
    font-weight: 900;
    text-transform: uppercase;
    line-height: 1.15;
  }
  .brand__dot {
    width: 22px;
    height: 22px;
    border-radius: 50%;
    background: var(--gold);
  }
  .card--front .brand {
    position: absolute;
    top: 70px;
    left: 0;
    right: 0;
    font-size: 30px;
    letter-spacing: 1px;
  }
  .web {
    position: absolute;
    right: 40px;
    bottom: 32px;
    color: var(--navy);
    font-weight: 700;
    font-size: 19px;
  }

  .back__brand-side {
    width: 52%;
    display: flex;
    align-items: center;
    justify-content: center;
    background: var(--paper);
  }
  .back__brand-side .brand {
    font-size: 22px;
    letter-spacing: 0.5px;
  }
  .back__info {
    width: 48%;
    background: var(--navy);
    color: var(--white);
    text-align: center;
    padding: 38px 18px 0;
  }
  .person__name {
    color: var(--gold);
    font-weight: 700;
    font-size: 22px;
    letter-spacing: 0.5px;
  }
  .person__title {
    font-size: 15px;
    margin-top: 4px;
  }
  .phones {
    list-style: none;
    margin: 44px 0 0 26px;
    text-align: left;
  }
  .phones li {
    display: flex;
    align-items: center;
    gap: 10px;
    font-size: 17px;
    margin-bottom: 12px;
  }
  .icon {
    width: 24px;
    height: 24px;
    flex: none;
  }
  .details {
    margin-top: 34px;
    font-size: 17px;
    line-height: 1.45;
  }
  .details dt {
    display: inline;
    color: var(--gold);
    font-weight: 700;
  }
  .details dd { display: inline; }
</style>
</head>
<body>
<main class="stage">

  <section class="card card--front" aria-label="Card front">
    <div class="brand">
      <span class="brand__dot"></span>
      <span>Brackenford<br>Guard Service</span>
    </div>
    <p class="web">www.brackenfordguardservice.com.au</p>
  </section>

  <section class="card card--back" aria-label="Card back">
    <div class="back__brand-side">
      <div class="brand">
        <span class="brand__dot"></span>
        <span>Brackenford<br>Guard Service</span>
      </div>
    </div>
    <div class="back__info">
      <h1 class="person__name">COLIN PARSNOW</h1>
      <p class="person__title">General Manager</p>

      <ul class="phones">
        <li>
          <svg class="icon" viewBox="0 0 24 24" aria-hidden="true">
            <circle cx="12" cy="12" r="12" fill="var(--gold)"/>
            <path d="M8.2 5.8c.4-.3 1-.2 1.3.2l1.3 2c.3.4.2 1-.2 1.3l-.9.7c.6 1.5 1.8 2.8 3.3 3.5l.7-.9c.3-.4.9-.5 1.3-.2l2 1.3c.4.3.5.9.2 1.3l-.8 1.2c-.5.6-1.3.9-2.1.6-3.4-1.2-6-3.9-7.1-7.2-.3-.8 0-1.6.6-2.1z" fill="var(--navy)"/>
          </svg>
          045 02 7163 2987
        </li>
        <li>
          <svg class="icon" viewBox="0 0 24 24" aria-hidden="true">
            <circle cx="12" cy="12" r="12" fill="var(--gold)"/>
            <rect x="8" y="5" width="8" height="14" rx="1.5" fill="var(--navy)"/>
            <rect x="9.3" y="7" width="5.4" height="6.5" fill="var(--gold)"/>
            <circle cx="12" cy="16.3" r="1" fill="var(--gold)"/>
          </svg>
          0438 725 914
        </li>
      </ul>

      <dl class="details">
        <div><dt>ABN:</dt> <dd>62 417 390 518</dd></div>
        <div><dt>Master License:</dt> <dd>536 918 407</dd></div>
        <div><dt>Address:</dt> <dd>P.O.Box 358 Elmcrest<br>NSW 2061</dd></div>
      </dl>
    </div>
  </section>

</main>
</body>
</html>
```